Viral food truck (ClipBuzz) needs menu

Our food truck has gone viral on ClipBuzz and we're now requesting a one-page food menu for a taco food truck, please use the logo attached as inspiration and stick to those colors when designing the menu. This is a bilingual menu, please ensure to make the English translation stand out as well.

Size: 8x12 landscape

LOGO - Morales's Taco Bar
318 W Orchard Ln (Entrada/Entrance Brightway Shopping Center)
Central Islip, NY 11548
Fri, 6 pm to 11:30 pm | Sat, 1 pm to 11:30 pm | Sun, 1 pm to 11:00 pm

Para horario y información / For pop-up, updated hours and information
Síganos/Follow Us: @moralestacobar

MENU

Tacos.....$4.75 ea
Selección de carne, cilantro, cebolla, salsa roja o verde
Choice of meat, cilantro, onion, red or green salsa

Selección de carne/Choice of Meat
Pollo (Chicken)
Carne Asada (Steak)
Al pastor (Marinated Pork)
Chorizo (Sausage)
Carnitas (Pulled Pork)
Mixta (steak & sausage)........$0.75 extra
Suadero (Brisket).......$0.75 extra
Lengua (Beef Tongue)......$0.75 extra
Tripa (Beef Tripe)......$0.75 extra

Antojitos/Appetizers
Tacos Dorados De Pollo.......$15.00
Taco Dorados De Carne.........$15.00
Quesadilla...........$10.00
Pollo (Chicken) | Carne Asada (Steak) | Queso (Cheese)
Pupusa Revueltas (Chicharone y Queso).........$3.50
Pupusa Queso............$3.50

Especiales / Specials
(#1) 4 Tacos..........$14
(#2) 4 Tacos Dorados/Flautas
Pollo, Creama, Queso Fresco, Aguacate
Chicken, Cream, Queso Fresco, Avocado
*(designer note: need a symbol here) (#3) Chicharones 1lb........$25.00

* Cantidad limitada y temoprada/Limited Quantity/Seasonal

BEBIDAS/BEVERAGES

Horchata.........$6.00

Agua Fresca.......$5.00
SABOR/FLAVOR
Limonada (Lemonade) | Jamaica (Hibiscus) | Sandia (Watermelon) | Piña (Pineapple) | Melon | Mango

Fizzo......$2.00
Zestle.....$2.00
Water.....$1.50
Bubblitos.......$3.00

Target Market(s)

Foodies

Industry/Entity Type

Food truck

Font styles to use
Sans Serif

Colors

Designer to choose colors to be used in the design.

Requirements
Must have
• Color and elements based on our logo, please also visit our Pictagram and Friendbook page for inspiration
Nice to have
• Vintage esthetic

```html
<!DOCTYPE html>
<html lang="en">
<head>
<meta charset="utf-8">
<title>Morales's Taco Bar – Menu</title>
<link href="https://fonts.googleapis.com/css2?family=Anton&family=Kanit:wght@300;400;500&display=swap" rel="stylesheet">
<style>
  :root {
    --paper: #f6f6f6;
    --orange-light: #d98410;
    --orange-mid: #c65f14;
    --orange-deep: #9a330d;
    --brush: #ee8427;
    --red: #e11f26;
    --cream: #fdf1e3;
    --menu-word: #e57c20;
    --brown: #3a1a06;
    --logo-ring: #2a1a0e;
    --logo-fill: #f1dcb4;
  }
  * { box-sizing: border-box; margin: 0; padding: 0; }
  html, body { width: 1200px; height: 904px; overflow: hidden; background: #fff; }
  .menu-sheet {
    position: relative; width: 1200px; height: 904px; overflow: hidden;
    background: var(--paper);
    font-family: "Kanit", sans-serif; font-weight: 300; color: var(--cream);
  }
  .backdrop { position: absolute; inset: 0; }
  .photo { position: absolute; }
  .photo--quesadilla { left: 266px; top: 0; width: 300px; height: 355px;
    background: linear-gradient(150deg, #f3d7a8, #e0a257 55%, #f4efe6); }
  .photo--tacos { left: 54px; top: 242px; width: 390px; height: 390px; border-radius: 50%;
    background: radial-gradient(circle, #a9c06a 0%, #d7b98a 45%, #cdb08a 70%, #bfa27c 100%); }
  .photo--steak { left: -13px; top: 626px; width: 292px; height: 292px; border-radius: 50%;
    background: radial-gradient(circle at 45% 60%, #5a2c18 0%, #c7893d 45%, #eeeeea 75%); }
  .photo--horchata { left: 279px; top: 664px; width: 165px; height: 240px;
    background: linear-gradient(180deg, #f3eee6, #e9e2d6 60%, #f6f3ee); border-radius: 10px 10px 0 0; }
  .photo--cutlery { left: 480px; top: 390px; width: 80px; height: 120px;
    background: linear-gradient(135deg, #e2e4e6, #c4c7ca); border-radius: 40px; opacity: .6; }

  .brand-mark { position: absolute; border-radius: 50%; display: flex; align-items: center;
    justify-content: center; text-align: center; background: var(--logo-fill);
    border: 4px solid var(--logo-ring); color: var(--logo-ring); font-family: "Kanit", sans-serif;
    font-weight: 500; line-height: 1.1; }
  .brand-mark--corner { left: 31px; top: 21px; width: 170px; height: 170px; font-size: 19px; }
  .brand-mark--center { left: 645px; top: 415px; width: 150px; height: 150px; font-size: 17px; }

  .menu-word { position: absolute; left: 626px; top: 280px; font-family: "Anton", sans-serif;
    font-size: 118px; line-height: 1; letter-spacing: 0; color: var(--menu-word);
    transform: scaleX(0.82); transform-origin: left top; white-space: nowrap; }

  .venue { position: absolute; left: 648px; font-size: 12.5px; line-height: 15px; }
  .venue--address { top: 572px; }
  .hours-band { position: absolute; left: 618px; top: 634px; width: 225px; height: 74px;
    background: var(--brush); clip-path: polygon(2% 6%, 98% 0, 100% 30%, 97% 62%, 100% 96%, 4% 100%, 0 70%, 3% 38%); }
  .venue--hours { top: 637px; font-size: 15px; line-height: 18.5px; font-weight: 400; }
  .venue--info { top: 713px; }
  .venue--social { top: 764px; }
  .footnote { position: absolute; left: 423px; top: 850px; font-size: 10.5px; color: var(--brown); }

  .menu-column { position: absolute; left: 871px; width: 277px; font-size: 12px; line-height: 15.1px; }
  .menu-column--wide { width: 305px; }
  .section-head { position: absolute; left: 850px; width: 305px; height: 20px;
    background: var(--brush); font-weight: 400; font-size: 13.5px; line-height: 20px;
    padding: 0 8px 0 21px; color: var(--cream); text-transform: uppercase;
    clip-path: polygon(0 30%, 4% 0, 96% 8%, 100% 40%, 97% 100%, 2% 92%); }
  .price-row { display: flex; align-items: baseline; white-space: nowrap; }
  .price-row .leader { flex: 1; border-bottom: 1px dotted var(--cream); margin: 0 1px 3px; opacity: .85; }
  .head-row { display: flex; white-space: nowrap; }
  .head-row .leader { flex: 1; border-bottom: 1px dotted var(--cream); margin: 0 2px 5px; }
  .gap { height: 15px; }
</style>
</head>
<body>
<main class="menu-sheet">
  <svg class="backdrop" width="1200" height="904" viewBox="0 0 1200 904" aria-hidden="true">
    <defs>
      <linearGradient id="panelTone" x1="0" y1="0" x2="1" y2="0.3">
        <stop offset="0" stop-color="#d98410"/>
        <stop offset="0.45" stop-color="#cf6f12"/>
        <stop offset="0.8" stop-color="#b94a10"/>
        <stop offset="1" stop-color="#8e2e0c"/>
      </linearGradient>
    </defs>
    <path d="M450 0 C 560 120, 600 300, 560 520 C 530 700, 420 830, 300 904 L 282 904 C 400 820, 510 690, 540 520 C 575 320, 545 140, 450 0 Z" fill="var(--red)"/>
    <path d="M462 0 C 575 120, 612 300, 573 520 C 545 700, 440 830, 320 904 L 1200 904 L 1200 0 Z" fill="url(#panelTone)"/>
  </svg>

  <div class="photo photo--quesadilla" role="img" aria-label="Photo of a golden grilled quesadilla cut into wedges"></div>
  <div class="photo photo--tacos" role="img" aria-label="Photo of three chicken tacos with pico de gallo and guacamole on a plate"></div>
  <div class="photo photo--steak" role="img" aria-label="Photo of grilled steak with potato wedges and salad"></div>
  <div class="photo photo--cutlery" role="img" aria-label="Photo of a spoon and fork"></div>
  <div class="photo photo--horchata" role="img" aria-label="Photo of a glass of horchata with cinnamon stick and metal straw"></div>

  <div class="brand-mark brand-mark--corner">Morales's<br>Taco Bar</div>

  <div class="menu-word">MENU</div>
  <div class="brand-mark brand-mark--center">Morales's<br>Taco Bar</div>

  <p class="venue venue--address">318 W Orchard Ln (Entrada/<br>Entrance Brightway Shopping Center)<br>Central Islip, NY 11548</p>
  <div class="hours-band"></div>
  <p class="venue venue--hours">FRI, 6 PM TO 11:30 PM<br>SAT, 1 PM TO 11:30 PM<br>SUN, 1 PM TO 11:00 PM</p>
  <p class="venue venue--info">Para horario y información /<br>For pop-up, updated hours<br>and information</p>
  <p class="venue venue--social">Síganos/Follow Us:<br>@moralestacobar</p>
  <p class="footnote">* Cantidad limitada y temoprada/Limited Quantity/Seasonal</p>

  <div class="section-head" style="top:34px"><div class="head-row"><span>Tacos</span><span class="leader"></span><span>$4.75 EA</span></div></div>
  <div class="menu-column menu-column--wide" style="top:58px">
    <p>Selección de carne, cilantro, cebolla, salsa roja o verde</p>
    <p>Choice of meat, cilantro, onion, red or green salsa</p>
  </div>

  <div class="section-head" style="top:105px">Selección de carne/Choice of meat</div>
  <div class="menu-column" style="top:130px">
    <div class="price-row"><span>Pollo (Chicken)</span><span class="leader"></span><span>$0.00 extra</span></div>
    <div class="price-row"><span>Carne Asada (Steak)</span><span class="leader"></span><span>$0.00 extra</span></div>
    <div class="price-row"><span>Al pastor (Marinated Pork)</span><span class="leader"></span><span>$0.00 extra</span></div>
    <div class="price-row"><span>Chorizo (Sausage)</span><span class="leader"></span><span>$0.00 extra</span></div>
    <div class="price-row"><span>Carnitas (Pulled Pork)</span><span class="leader"></span><span>$0.00 extra</span></div>
    <div class="price-row"><span>Mixta (steak &amp; sausage)</span><span class="leader"></span><span>$0.75 extra</span></div>
    <div class="price-row"><span>Suadero (Brisket)</span><span class="leader"></span><span>$0.75 extra</span></div>
    <div class="price-row"><span>Lengua (Beef Tongue)</span><span class="leader"></span><span>$0.75 extra</span></div>
    <div class="price-row"><span>Tripa (Beef Tripe)</span><span class="leader"></span><span>$0.75 extra</span></div>
  </div>

  <div class="section-head" style="top:284px">Antojitos/Appetizers</div>
  <div class="menu-column" style="top:310px">
    <div class="price-row"><span>Tacos Dorados De Pollo</span><span class="leader"></span><span>$15.00</span></div>
    <div class="price-row"><span>Taco Dorados De Carne</span><span class="leader"></span><span>$15.00</span></div>
    <div class="price-row"><span>Quesadilla</span><span class="leader"></span><span>$10.00</span></div>
    <p>Pollo (Chicken) | Carne Asada (Steak)</p>
    <p>Queso (Cheese) | Pupusa Revueltas</p>
    <div class="price-row"><span>(Chicharone y Queso)</span><span class="leader"></span><span>$3.50</span></div>
    <div class="price-row"><span>Pupusa Queso</span><span class="leader"></span><span>$3.50</span></div>
  </div>

  <div class="section-head" style="top:436px">Especiales / Specials</div>
  <div class="menu-column" style="top:460px; width:270px">
    <div class="price-row"><span>(#1) 4 Tacos</span><span class="leader"></span><span>$14.00</span></div>
    <p>Selección de carne, cilantro, cebolla,</p>
    <p>salsa roja o verde</p>
    <p>Choice of meat, cilantro, onion,</p>
    <p>red or green salsa</p>
    <div class="gap"></div>
    <div class="price-row"><span>(#2) 4 Tacos Dorados/Flautas</span><span class="leader"></span><span>$0.00</span></div>
    <p>Pollo, Creama, Queso Fresco, Aguacate</p>
    <p>Chicken, Cream, Queso Fresco, Avocado</p>
    <div class="gap"></div>
    <div class="price-row"><span>(#3) Chicharones 1lb</span><span class="leader"></span><span>$25.00</span></div>
  </div>

  <div class="section-head" style="top:653px">Bebidas/Beverages</div>
  <div class="menu-column" style="top:677px">
    <div class="price-row"><span>Horchata</span><span class="leader"></span><span>$6.00</span></div>
    <div class="price-row"><span>Agua Fresca</span><span class="leader"></span><span>$5.00</span></div>
  </div>

  <div class="section-head" style="top:722px">Sabor/Flavor</div>
  <div class="menu-column" style="top:748px">
    <p>Limonada (Lemonade) | Jamaica (Hibiscus)</p>
    <p>Sandia (Watermelon) | Piña (Pineapple)</p>
    <p>Melon | Mango</p>
  </div>
  <div class="menu-column" style="top:803px">
    <div class="price-row"><span>Fizzo</span><span class="leader"></span><span>$2.00</span></div>
    <div class="price-row"><span>Zestle</span><span class="leader"></span><span>$2.00</span></div>
    <div class="price-row"><span>Water</span><span class="leader"></span><span>$1.50</span></div>
    <div class="price-row"><span>Bubblitos</span><span class="leader"></span><span>$3.00</span></div>
  </div>
</main>
</body>
</html>
```